Complete Stationary Package for Harbor Chapel
Harbor Chapel -- The Believers of Redfield (under Harbor Chapel and smaller)
Complete Stationary Package for Harbor Chapel  - Religion and Spirituality
Creative Brief
Use specific fonts
new, vibrant, creative (please see comments below -- suprise and impress me!))
Bright & Fun-filled
Martin Delvaux
Pastor
418 W. Brinley Ave Longview, TX 75612
hcredfield@mailnest.example
harborredfield.example
I love this logo, the shape and the concept and the way the c and the t work together. However, I would like stationary designers to please use a much more creative font. Also, feel free to change, enhance the colors of the logo itself as you feel is best.
OPTION ONE Service Times Prayer Sunday 10 am Friday 7 pm Sunday 6 pm Youth Service Wednesday 7 pm Friday 8 pm OPTION TWO Harbor Chapel The Believers of Redfield www.harborredfield.example I would like to see both options if possible in order to help me decide which works best. Thanks!
kmrowell kmrowell
Please use avatars for all information such as phone, email, website, etc.
Designers: Thanks for your wonderful contributions! I have uploaded an another version of the same logo that may look a lot better against a solid background. It may be that one looks good on a white back ground, the other on a solid background. Please help me make this determination. Also, know that I am willing to provide extra compensation for extra effort. Thanks! Martin
Also, please show designs with at least a couple of different fonts. Thanks!
Clarification: The following information should read -- Services Sunday 10 am Sunday 6 pm Wednesday 7 pm Prayer Friday 7 pm Youth Service / Activities Friday 8 pm Thanks!
Thanks for the immediate response to this contest! We're off to a fantastic start! Please keep in mind that I'm looking for a complete stationary package -- folder, letterhead, envelopes, electronic signature, cd labels, etc.

```html
<!DOCTYPE html>
<html lang="en">
<head>
<meta charset="utf-8">
<title>Harbor Chapel – Business Card</title>
<link rel="stylesheet" href="https://fonts.googleapis.com/css2?family=Cinzel:wght@400;600&family=Lora:wght@400;500&display=swap">
<style>
  :root {
    --stage: #ece7df;
    --blue-deep: #0b3f93;
    --blue-mid: #1769c9;
    --blue-light: #3aa5ee;
    --orange-deep: #e05300;
    --orange-mid: #f57b12;
    --orange-light: #ffa431;
    --leaf-dark: #2f8f1e;
    --leaf-light: #a6dc3c;
    --ink-light: #ffffff;
    --ink-soft: rgba(255,255,255,0.9);
  }
  * { box-sizing: border-box; margin: 0; padding: 0; }
  html, body { width: 1200px; height: 696px; overflow: hidden; }
  body {
    background: var(--stage);
    display: flex;
    align-items: center;
    justify-content: center;
    gap: 60px;
    font-family: "Lora", Georgia, serif;
    color: var(--ink-light);
  }
  .card {
    position: relative;
    width: 520px;
    height: 300px;
    border-radius: 18px;
    overflow: hidden;
    box-shadow: 0 10px 28px rgba(0,0,0,0.22);
  }
  .card--front {
    background: linear-gradient(135deg, var(--blue-light) 0%, var(--blue-mid) 45%, var(--blue-deep) 100%);
  }
  .card--back {
    background: radial-gradient(circle at 40% 30%, var(--orange-light) 0%, var(--orange-mid) 45%, var(--orange-deep) 100%);
  }
  .leaf-art { position: absolute; display: block; }
  .leaf-art--front { top: 0; right: 0; width: 190px; height: 130px; }
  .leaf-art--back { left: 0; bottom: 0; width: 520px; height: 130px; }

  .brand {
    position: absolute;
    top: 70px;
    left: 130px;
    display: flex;
    align-items: center;
    gap: 12px;
  }
  .brand__dot {
    width: 46px; height: 46px;
    border-radius: 50%;
    background: var(--orange-mid);
    flex: none;
  }
  .brand__name {
    font-family: "Cinzel", Georgia, serif;
    font-weight: 600;
    font-size: 26px;
    letter-spacing: 1px;
    white-space: nowrap;
  }
  .identity {
    position: absolute;
    left: 26px;
    top: 150px;
  }
  .identity__name {
    font-family: "Cinzel", Georgia, serif;
    font-size: 17px;
    letter-spacing: 1.5px;
  }
  .identity__role {
    font-size: 12px;
    color: var(--ink-soft);
    margin-top: 2px;
  }
  .contact {
    position: absolute;
    left: 26px;
    bottom: 20px;
    list-style: none;
    font-size: 11px;
    line-height: 1.55;
    color: var(--ink-soft);
  }
  .contact li { display: flex; align-items: center; gap: 7px; white-space: nowrap; }
  .contact svg { width: 11px; height: 11px; flex: none; }

  .services {
    position: absolute;
    top: 26px;
    font-size: 12px;
    line-height: 1.5;
  }
  .services--main { left: 30px; }
  .services--extra { left: 210px; }
  .services__heading {
    font-family: "Cinzel", Georgia, serif;
    font-weight: 600;
    font-size: 14px;
    letter-spacing: 1px;
    margin-top: 6px;
  }
  .services__heading:first-child { margin-top: 0; }
  .services__time { color: var(--ink-soft); }
</style>
</head>
<body>

<section class="card card--front" aria-label="Business card front">
  <svg class="leaf-art leaf-art--front" viewBox="0 0 190 130" role="img" aria-label="Green leaf illustration">
    <defs>
      <linearGradient id="leafFront" x1="0" y1="1" x2="1" y2="0">
        <stop offset="0" stop-color="#2f8f1e"/>
        <stop offset="1" stop-color="#a6dc3c"/>
      </linearGradient>
    </defs>
    <path d="M190 0 H60 C80 50 130 110 190 130 Z" fill="url(#leafFront)"/>
  </svg>

  <div class="brand">
    <span class="brand__dot"></span>
    <span class="brand__name">Harbor Chapel</span>
  </div>

  <div class="identity">
    <p class="identity__name">Martin Delvaux</p>
    <p class="identity__role">Pastor</p>
  </div>

  <ul class="contact">
    <li>
      <svg viewBox="0 0 12 12"><path d="M6 0.5a3.6 3.6 0 0 0-3.6 3.6C2.4 7 6 11.5 6 11.5S9.6 7 9.6 4.1A3.6 3.6 0 0 0 6 .5zm0 5a1.4 1.4 0 1 1 0-2.8 1.4 1.4 0 0 1 0 2.8z" fill="#fff"/></svg>
      418 W. Brinley Ave Longview, TX 75612
    </li>
    <li>
      <svg viewBox="0 0 12 12"><path d="M3 .8l1.8 2.4-1 1.2c.7 1.5 1.9 2.7 3.4 3.4l1.2-1 2.4 1.8-.8 2.2C5.5 10.6 1.4 6.5.8 1.6z" fill="#fff"/></svg>
      (903) 555-0148
    </li>
    <li>
      <svg viewBox="0 0 12 12"><rect x=".8" y="2.2" width="10.4" height="7.6" rx="1" fill="none" stroke="#fff"/><path d="M1 2.6 6 6.6l5-4" fill="none" stroke="#fff"/></svg>
      hcredfield@mailnest.example
    </li>
    <li>
      <svg viewBox="0 0 12 12"><circle cx="6" cy="6" r="5" fill="none" stroke="#fff"/><path d="M1 6h10M6 1c2 2.5 2 7.5 0 10M6 1c-2 2.5-2 7.5 0 10" fill="none" stroke="#fff" stroke-width=".8"/></svg>
      www.harborredfield.example
    </li>
  </ul>
</section>

<section class="card card--back" aria-label="Business card back">
  <div class="services services--main">
    <p class="services__heading">Services</p>
    <p class="services__time">Sunday 10 am</p>
    <p class="services__time">Sunday 6 pm</p>
    <p class="services__time">Wednesday 7 pm</p>
  </div>
  <div class="services services--extra">
    <p class="services__heading">Prayer</p>
    <p class="services__time">Friday 7 pm</p>
    <p class="services__heading">Youth Service</p>
    <p class="services__time">Friday 8 pm</p>
  </div>

  <svg class="leaf-art leaf-art--back" viewBox="0 0 520 130" role="img" aria-label="Green leaf illustration sweeping across the card">
    <defs>
      <linearGradient id="leafBack" x1="0" y1="1" x2="1" y2="0">
        <stop offset="0" stop-color="#2f8f1e"/>
        <stop offset="1" stop-color="#a6dc3c"/>
      </linearGradient>
    </defs>
    <path d="M0 130 V70 C150 20 360 30 520 50 V130 Z" fill="url(#leafBack)"/>
  </svg>
</section>

</body>
</html>
```